Helicopter scenic /Charter company

Need a sign 920mm x 920mm for our Marlow Helipad fence that catches the eye for people walking past. Some photos have been attached but feel free to use helicopter photos you have as well. Like the sign to be black with lettering that stands out. You may do a design with photos or it may look better without. It is up to you. It just has to look eye catching and exciting.
Text: Helicopter Joy Flights & Scenic Tours here seven days from October to March. Prices from just $99 per person* Details at wendaloft.com.au or ph 9372 6105
* $99 flights are shared 8 minute flights and are only available on weekends

Target Market(s)

Tourists locals walking past the helipad

Requirements
Must have
• Logo
• Text as in project description

```html
<!DOCTYPE html>
<html lang="en">
<head>
<meta charset="utf-8">
<title>Helicopter Joy Flights &amp; Scenic Tours – Fence Sign</title>
<link rel="stylesheet" href="https://fonts.googleapis.com/css2?family=Audiowide&family=Source+Sans+3:wght@400;600;700&family=Arimo&display=swap">
<style>
  :root {
    --charcoal: #36363a;
    --black: #000000;
    --navy: #1c3f7c;
    --sky-top: #0b8fd6;
    --sky-mid: #3aa9e4;
    --sky-low: #bfe3f7;
    --heli-white: #eef3f6;
    --heli-teal: #2e9c93;
    --yellow: #ffd200;
    --white: #ffffff;
    --grey-name: #b9b9bc;
  }
  html, body {
    margin: 0;
    padding: 0;
    width: 1200px;
    height: 1200px;
    overflow: hidden;
    background: var(--black);
  }
  .sign {
    position: relative;
    width: 1200px;
    height: 1200px;
    overflow: hidden;
    font-family: "Source Sans 3", sans-serif;
  }
  .backdrop {
    position: absolute;
    inset: 0;
  }
  .headline {
    position: absolute;
    left: 89px;
    top: 51px;
    margin: 0;
    font-family: "Audiowide", sans-serif;
    font-style: italic;
    font-weight: 400;
    font-size: 64px;
    line-height: 68px;
    letter-spacing: 1px;
    color: var(--yellow);
    text-transform: uppercase;
    white-space: nowrap;
  }
  .season-banner {
    position: absolute;
    left: 124px;
    top: 371px;
    width: 950px;
    height: 133px;
  }
  .season-banner svg { position: absolute; inset: 0; }
  .season-text {
    position: absolute;
    inset: 0;
    display: flex;
    align-items: center;
    justify-content: center;
    gap: 14px;
    font-size: 50px;
    color: var(--white);
    white-space: nowrap;
  }
  .season-text .hl { color: var(--yellow); font-weight: 600; }
  .season-text .big-seven {
    color: var(--yellow);
    font-size: 104px;
    font-weight: 400;
    line-height: 1;
    margin-top: 8px;
  }
  .price-badge {
    position: absolute;
    left: 20px;
    top: 580px;
    width: 412px;
    height: 360px;
  }
  .price-badge svg { position: absolute; inset: 0; }
  .price-text {
    position: absolute;
    inset: 0;
    display: flex;
    flex-direction: column;
    align-items: center;
    color: var(--white);
  }
  .price-text .lead { margin-top: 24px; font-size: 48px; font-weight: 600; color: var(--yellow); line-height: 1; }
  .price-text .from { font-size: 38px; line-height: 1.1; }
  .price-text .amount { font-size: 168px; font-weight: 600; color: var(--yellow); line-height: 0.92; margin-top: 2px; letter-spacing: -3px; }
  .price-text .per { font-size: 31px; margin-top: 6px; }
  .brand {
    position: absolute;
    left: 54px;
    top: 1030px;
    display: flex;
    align-items: center;
    gap: 18px;
  }
  .brand-dot {
    width: 78px;
    height: 78px;
    border-radius: 50%;
    background: var(--yellow);
  }
  .brand-name {
    font-weight: 700;
    font-size: 52px;
    line-height: 44px;
    letter-spacing: 1px;
    color: var(--grey-name);
    text-transform: uppercase;
  }
  .web {
    position: absolute;
    right: 88px;
    top: 974px;
    font-size: 42px;
    letter-spacing: 1px;
    color: var(--white);
  }
  .web .domain { color: var(--yellow); }
  .phone {
    position: absolute;
    left: 642px;
    top: 1036px;
    display: flex;
    align-items: center;
    gap: 28px;
  }
  .phone-number {
    font-size: 84px;
    font-weight: 600;
    color: var(--yellow);
    line-height: 1;
  }
  .footnote {
    position: absolute;
    left: 0;
    right: 0;
    top: 1152px;
    margin: 0;
    text-align: center;
    font-family: "Arimo", sans-serif;
    font-size: 27px;
    line-height: 32px;
    color: var(--yellow);
  }
</style>
</head>
<body>
<main class="sign">
  <svg class="backdrop" width="1200" height="1200" viewBox="0 0 1200 1200">
    <defs>
      <linearGradient id="skyGradient" x1="0" y1="0" x2="0.3" y2="1">
        <stop offset="0" stop-color="var(--sky-top)"/>
        <stop offset="0.55" stop-color="var(--sky-mid)"/>
        <stop offset="1" stop-color="var(--sky-low)"/>
      </linearGradient>
      <radialGradient id="helicopterGlow" cx="0.5" cy="0.5" r="0.5">
        <stop offset="0" stop-color="var(--heli-white)" stop-opacity="0.95"/>
        <stop offset="0.55" stop-color="var(--heli-teal)" stop-opacity="0.55"/>
        <stop offset="1" stop-color="var(--heli-teal)" stop-opacity="0"/>
      </radialGradient>
    </defs>
    <rect class="sky-photo" x="0" y="150" width="1200" height="870" fill="url(#skyGradient)" role="img" aria-label="Photo of a blue sky with light clouds"/>
    <ellipse class="helicopter-photo" cx="790" cy="745" rx="380" ry="175" fill="url(#helicopterGlow)" role="img" aria-label="Photo of a white and teal helicopter in flight, banking to the left"/>
    <polygon class="navy-wedge" points="764,260 1200,186 1200,345" fill="var(--navy)"/>
    <polygon class="black-stripe" points="0,0 1200,0 1200,186 0,382" fill="var(--black)"/>
    <polygon class="charcoal-band" points="0,0 1200,0 1200,143 0,377" fill="var(--charcoal)"/>
    <polygon class="footer-band" points="0,998 1200,881 1200,1200 0,1200" fill="var(--black)"/>
  </svg>

  <h1 class="headline">Helicopter Joy Flights<br>&amp; Scenic Tours</h1>

  <div class="season-banner">
    <svg width="950" height="133" viewBox="0 0 950 133">
      <polygon points="40,0 910,0 950,40 950,93 910,133 40,133 0,93 0,40" fill="var(--black)"/>
      <polygon points="44,10 906,10 940,44 940,89 906,123 44,123 10,89 10,44" fill="none" stroke="var(--white)" stroke-width="2.5"/>
    </svg>
    <div class="season-text">
      <span class="big-seven">7</span>
      <span><span class="hl">Days</span> from <span class="hl">October</span> to <span class="hl">March.</span></span>
    </div>
  </div>

  <div class="price-badge">
    <svg width="412" height="360" viewBox="0 0 412 360">
      <polygon points="0,180 103,0 309,0 412,180 309,360 103,360" fill="var(--black)"/>
      <polygon points="13,180 109,12 303,12 399,180 303,348 109,348" fill="none" stroke="var(--white)" stroke-width="2.5"/>
    </svg>
    <div class="price-text">
      <span class="lead">Prices</span>
      <span class="from">from just</span>
      <span class="amount">$99</span>
      <span class="per">per person*</span>
    </div>
  </div>

  <div class="brand">
    <span class="brand-dot"></span>
    <span class="brand-name">Wendaloft<br>Helicopters</span>
  </div>

  <div class="web">www.<span class="domain">wendaloft.com.au</span></div>

  <div class="phone">
    <svg class="phone-icon" width="74" height="74" viewBox="0 0 74 74" aria-hidden="true">
      <circle cx="37" cy="37" r="33" fill="none" stroke="var(--white)" stroke-width="5"/>
      <path d="M26 18c3 0 6 7 6 9s-4 3-4 5c0 3 8 12 11 12 2 0 3-4 5-4s9 3 9 6-4 8-8 8c-10 0-24-15-24-26 0-4 3-10 5-10z" fill="var(--white)"/>
      <path d="M42 22a12 12 0 0 1 10 10M42 15a19 19 0 0 1 17 17" fill="none" stroke="var(--white)" stroke-width="3" stroke-linecap="round"/>
    </svg>
    <span class="phone-number">9372 6105</span>
  </div>

  <p class="footnote">* $99 flights are shared 8 minute flights and are only available on weekends</p>
</main>
</body>
</html>
```